Redesign, cleanup and edit my Presentations

I have a series of power points that I use for training purposes. They were made by me over time. During the last couple years, I have evolved their look and content over time, but not consistently. More specifically, I have not gone back to re-edit the older decks. So, some decks are too wordy, too long, or and don't look consistent.

I am looking someone who can create a good design that I can use going forward, and who could also apply that theme to the existing decks, along with editing the existing, and future decks, too.

I have a lot of slides to produce and/or edit -approximately 500. But this request is a test to find a powerpoint partner. I am supplying 2 decks. One that's older and more wordy than the other. I would like to see what you would suggest we do differently. So that's what you are bidding on today. Also, you do not have to complete deck "Phase 4.7." I only need enough of the deck done to see where you would take it. Maybe 10 slides? Your choice. However, with that deck, there are lots of opportunities to clarify, re-align, and minimize within that deck.

But, if you are selected, I want to engage with you on an ongoing basis, and send more material your way. Then, you will be engaged to complete all decks.

Please ask me any questions to help you gain a better understanding of this project.

Target Market(s)

People in management, technical, medical, and financial fields who wish to become independent consultants.

Industry/Entity Type

Business Consultant

Font styles to use
Sans Serif

Requirements
Must have
• Use the existing color theme:
• yellow/gold - #f5b300,
• blue - 2b74a6
• Logo doesn't change
• Preferred fonts: Raleway for headings and Open Sans for general text
• Any pictures and graphics should have no copyright restrictions. That is, I should have use of the work without charge.
Nice to have
• I prefer a flat graphic style, although you can use pictures where it conveys a point more effectively.
• Ability to convert the presentations to Google Slides and Apple's Keynote apps.
• Ability to convert presentation to video
Should not have
• Restricted use graphics, photos, or other content.

```html
<!DOCTYPE html>
<html lang="en">
<head>
<meta charset="UTF-8">
<title>Step 1: Build a Background Profile</title>
<link href="https://fonts.googleapis.com/css2?family=Arimo:wght@700&family=Source+Sans+3:wght@400;600&display=swap" rel="stylesheet">
<style>
  :root {
    --gold: #f7b018;
    --blue: #1f78a8;
    --white: #ffffff;
  }
  * { margin: 0; padding: 0; box-sizing: border-box; }
  html, body { width: 1200px; height: 675px; overflow: hidden; background: var(--white); }
  .slide {
    position: relative;
    width: 1200px;
    height: 675px;
    background: var(--white);
    font-family: "Source Sans 3", "Myriad Pro", sans-serif;
  }
  .frame { position: absolute; left: 0; top: 0; }
  .step-label {
    position: absolute;
    left: 128px;
    top: 22px;
    font-family: "Arimo", Arial, sans-serif;
    font-weight: 700;
    font-size: 45px;
    color: var(--gold);
    line-height: 1;
  }
  .slide-title {
    position: absolute;
    left: 128px;
    top: 78px;
    font-family: "Arimo", Arial, sans-serif;
    font-weight: 700;
    font-size: 45px;
    letter-spacing: -0.2px;
    color: var(--blue);
    line-height: 1;
    white-space: nowrap;
  }
  .panel {
    position: absolute;
    top: 226px;
    width: 502px;
    height: 325px;
  }
  .panel--gold { left: 83px; background: var(--gold); }
  .panel--blue { left: 618px; background: var(--blue); }
  .avatar {
    position: absolute;
    top: 143px;
    width: 154px;
    height: 154px;
    border-radius: 50%;
    background: var(--white);
    box-shadow: 0 2px 6px rgba(0,0,0,0.25);
    display: flex;
    align-items: center;
    justify-content: center;
  }
  .avatar--left { left: 258px; }
  .avatar--right { left: 790px; }
  .avatar__figure {
    width: 104px;
    height: 104px;
    border-radius: 50%;
  }
  .avatar--left .avatar__figure { background: linear-gradient(180deg, #f1e2d3 0%, #3f82b4 100%); }
  .avatar--right .avatar__figure { background: linear-gradient(180deg, #f1e2d3 0%, #f39a28 100%); }
  .point__number {
    position: absolute;
    width: 38px;
    height: 38px;
    border: 2px solid var(--white);
    color: var(--white);
    font-family: "Arimo", Arial, sans-serif;
    font-weight: 700;
    font-size: 27px;
    display: flex;
    align-items: center;
    justify-content: center;
  }
  .point__text {
    position: absolute;
    color: var(--white);
    font-size: 20px;
    line-height: 24px;
    white-space: nowrap;
  }
  .brand {
    position: absolute;
    left: 953px;
    top: 594px;
    display: flex;
    align-items: center;
    gap: 8px;
  }
  .brand__dot {
    width: 44px;
    height: 44px;
    border-radius: 50%;
    background: var(--gold);
  }
  .brand__name {
    font-family: "Source Sans 3", sans-serif;
    font-weight: 600;
    font-size: 48px;
    line-height: 1;
    color: var(--blue);
  }
  .footer-band {
    position: absolute;
    left: 0;
    top: 655px;
    width: 1200px;
    height: 20px;
    background: var(--blue);
  }
</style>
</head>
<body>
<main class="slide">
  <svg class="frame" width="1200" height="675" viewBox="0 0 1200 675" aria-hidden="true">
    <polyline points="108,104 57,104 57,581 1145,581 1145,104 731,104" fill="none" stroke="var(--blue)" stroke-width="5"/>
  </svg>

  <p class="step-label">STEP 1:</p>
  <h1 class="slide-title">Build a Background Profile</h1>

  <section class="panel panel--gold"></section>
  <section class="panel panel--blue"></section>

  <div class="avatar avatar--left"><div class="avatar__figure" role="img" aria-label="Flat illustration of a man in a blue suit"></div></div>
  <div class="avatar avatar--right"><div class="avatar__figure" role="img" aria-label="Flat illustration of a woman in an orange suit"></div></div>

  <div class="point__number" style="left:93px;top:326px;">1</div>
  <p class="point__text" style="left:141px;top:318px;">Background, or demographics, is basic information<br>the starts to flesh out the persona.</p>

  <div class="point__number" style="left:93px;top:447px;">2</div>
  <p class="point__text" style="left:141px;top:398px;">For B2C personas, this can include age, gender, mar-<br>ital status, geographic location, education, career<br>information or any other demographic or biograph-<br>ic information that allows you to better empathize<br>with your target.</p>

  <div class="point__number" style="left:628px;top:319px;">3</div>
  <p class="point__text" style="left:676px;top:305px;">&nbsp;Thanks to your marketing previous market research<br>in Step 2,&nbsp; and/or through your keyword research,<br>you already have a lot of information. If you don’t,<br>try searching on demographic keywords, and con-<br>ducting more live interviews.</p>

  <div class="point__number" style="left:628px;top:456px;">4</div>
  <p class="point__text" style="left:676px;top:449px;">Be specific enough that you can visualize the perso-<br>na, but not so detailed that you limit who this per-<br>sona applies to.</p>

  <div class="brand">
    <span class="brand__dot"></span>
    <span class="brand__name">Veltano</span>
  </div>

  <div class="footer-band"></div>
</main>
</body>
</html>
```